依頼詳細
開店に合わせて駅前や既存店でチラシ(ポストカード)を配ろうと思います。そのチラシデザイン制作をお願い致します。サイズは100X148のポストカードサイズで両面作成お願い致します。店内は木(ウッド)を基調としカラーはアッシュ系でナチュラルな雰囲気をイメージしています。雑誌の1Pのようなとにかくお洒落なポストカードをお願い致します。現地住所の地図を入れて下さい。
記載項目
店名【Bistro MORUNE】
TEL:03-4172-9586
住所 東京都渋谷区渋谷4-3-27 青葉ビル1F
営業時間 ランチ 11:30~14:00(13:30L.O)
ディナー17:00~24:00(23:30L.O)
ロゴ (デザイン添付)

地図 (作成願います)
サイズ
100mmX148mm
ページ数
両面
希望イメージ
シンプル 複雑
単色 カラフル
暗い 明るい
日常 高級
遊び心 厳粛
未来的 伝統的
女性的 男性的
希望する色
納品ファイル
• イラストレーター形式 (.ai)
補足説明

```html
<!DOCTYPE html>
<html lang="ja">
<head>
<meta charset="utf-8">
<title>Bistro MORUNE — NEW OPEN</title>
<link rel="stylesheet" href="https://fonts.googleapis.com/css2?family=Noto+Serif+JP:wght@400;500;600&display=swap">
<style>
  :root {
    --paper: #ecebe8;
    --paper-edge: #e2e1dd;
    --ink: #1a1a1a;
    --shell-light: #f1efeb;
    --shell-mid: #cfc9c1;
    --shell-dark: #8f8880;
  }
  html, body {
    margin: 0;
    padding: 0;
    overflow: hidden;
    background: var(--paper);
  }
  .postcard {
    position: relative;
    width: 829px;
    height: 1200px;
    overflow: hidden;
    background: radial-gradient(ellipse at 50% 45%, var(--paper) 55%, var(--paper-edge) 100%);
    color: var(--ink);
    font-family: "Noto Serif JP", serif;
  }
  .headline {
    position: absolute;
    left: 58px;
    top: 52px;
    margin: 0;
    font-weight: 500;
    font-size: 118px;
    line-height: 1.16;
    letter-spacing: 2px;
  }
  .open-date {
    position: absolute;
    left: 60px;
    top: 325px;
    margin: 0;
    font-size: 62px;
    font-weight: 600;
    line-height: 1.2;
  }
  .open-date .weekday {
    font-size: 40px;
    font-weight: 500;
  }
  .open-place {
    position: absolute;
    left: 60px;
    top: 408px;
    margin: 0;
    font-size: 60px;
    font-weight: 600;
    line-height: 1.2;
  }
  .tagline {
    position: absolute;
    right: 165px;
    top: 48px;
    margin: 0;
    writing-mode: vertical-rl;
    transform: rotate(-25deg);
    transform-origin: top right;
    font-size: 27px;
    font-weight: 500;
    line-height: 1.55;
    letter-spacing: 3px;
  }
  .oyster-photo {
    position: absolute;
    left: 100px;
    top: 470px;
    width: 650px;
    height: 450px;
  }
  .concept {
    position: absolute;
    left: 118px;
    top: 905px;
    display: flex;
    align-items: center;
    gap: 48px;
  }
  .concept-icon {
    width: 56px;
    height: 112px;
  }
  .concept-text {
    margin: 0;
    font-size: 35px;
    font-weight: 500;
    line-height: 1.6;
    letter-spacing: 1px;
  }
  .shop-name {
    position: absolute;
    left: 360px;
    top: 1035px;
    margin: 0;
    font-size: 38px;
    font-weight: 600;
    letter-spacing: 2px;
    white-space: nowrap;
  }
</style>
</head>
<body>
  <main class="postcard">
    <h1 class="headline">NEW<br>OPEN</h1>
    <p class="open-date">9月18日<span class="weekday">(金)</span></p>
    <p class="open-place">@青山</p>

    <p class="tagline">オイスターバー<br>×<br>ビストロの<br>おいしい出会い</p>

    <svg class="oyster-photo" viewBox="0 0 650 460" role="img" aria-label="殻付きの生牡蠣の写真">
      <defs>
        <radialGradient id="oysterTone" cx="50%" cy="48%" r="60%">
          <stop offset="0%" stop-color="var(--shell-light)"/>
          <stop offset="55%" stop-color="var(--shell-mid)"/>
          <stop offset="100%" stop-color="var(--shell-dark)"/>
        </radialGradient>
      </defs>
      <path d="M40 150 C90 60 250 20 400 30 C540 40 630 120 615 230 C600 340 500 430 340 440 C190 450 60 390 30 290 C15 240 20 190 40 150 Z" fill="url(#oysterTone)"/>
    </svg>

    <section class="concept">
      <svg class="concept-icon" viewBox="0 0 58 128" aria-hidden="true">
        <path d="M4 4 H54 C56 40 48 66 31 72 V116 H46 V124 H12 V116 H27 V72 C10 66 2 40 4 4 Z" fill="var(--ink)"/>
      </svg>
      <p class="concept-text">新鮮で質のよい生牡蠣と<br>お酒で楽しむ大人のビストロ。</p>
    </section>

    <p class="shop-name">Bistro MORUNE</p>
  </main>
</body>
</html>
```